Business card design for Sable Crestway

We need business cards designed for our new marketing consulting company, Sable Crestway. Our services include marketing strategy, go-to-market and launch planning, growth strategy, and execution. We serve medical technology and health technology companies, from startups to well-established growth companies.

The business cards should feel professional, credible, reliable and trustworthy, and should instill confidence. Also bold, creative, and modern.

The design must use the Sable Crestway logo.

The primary brand color is this orange: #FF5501
A secondary color that you can use is this gray: #282B2D
I would prefer only to use the orange and gray. But if you feel you really need an additional accent color (please use it very sparingly, as little as possible), you can use this blue for small accent purposes: #009FED

Attached are the logo files. The main logo is the one with a little bit of orange on the left and the rest is gray.

The business card should include the following:

Sable Crestway logo
First name and last name
Title
Email address
Phone number and type (in whatever order looks best for the design
Website (the website does not need to be in the same block as the personal info)

For example:

Wren Tasker
Founder & Principal
wren@sablecrestway.com
+1.415.836.2094 mobile (can use "." or spaces in between blocks of numbers)
sablecrestway.com (somewhere on the card, it does not need to be with the personal info; and note that there is no "www." at the beginning)

Note that there will be no address listed on the business card.

Target Market(s)

Executives (CEO, head of marketing, head of sales) at medical technology and health technology companies, mostly in their 40s and older, well-educated, often with advanced degrees. They are strategic thinkers, responsible for budgets, and familiar with P&L. Their comfort with and trust in using outside consultants varies.

Industry/Entity Type

Medical technology and health technology companies.

Contact Information for Business Card

See project description

Font styles to use
Sans Serif

Requirements
Must have
• Logo and see Business card details section above.

```html
<!DOCTYPE html>
<html lang="en">
<head>
<meta charset="utf-8">
<title>Sable Crestway — Business Card</title>
<link href="https://fonts.googleapis.com/css2?family=Montserrat:wght@300;400;600;700&display=swap" rel="stylesheet">
<style>
  :root {
    --orange: #FF5501;
    --gray: #282B2D;
    --card-dark: #2a2d2f;
    --pattern-light: #3a3f42;
    --pattern-dark: #24272a;
    --white: #ffffff;
    --muted: #d9dcde;
    --backdrop: #1c1e1f;
  }
  * { margin: 0; padding: 0; box-sizing: border-box; }
  html, body { width: 1200px; height: 884px; overflow: hidden; }
  body {
    background: var(--backdrop);
    font-family: "Montserrat", Arial, sans-serif;
    display: flex;
    flex-direction: column;
    align-items: center;
    justify-content: center;
    gap: 40px;
  }
  .card {
    position: relative;
    width: 630px;
    height: 360px;
    border-radius: 18px;
    overflow: hidden;
    background: var(--card-dark);
    box-shadow: 0 10px 30px rgba(0,0,0,.45);
  }
  .panel-area { position: absolute; inset: 0; }
  .wordmark {
    position: absolute;
    display: flex;
    align-items: center;
    gap: 14px;
    color: var(--white);
  }
  .wordmark-dot {
    width: 30px; height: 30px;
    border-radius: 50%;
    background: var(--orange);
    flex: none;
  }
  .wordmark-name {
    font-weight: 600;
    font-size: 17px;
    line-height: 1.15;
    letter-spacing: .32em;
    text-transform: uppercase;
  }
  .front .wordmark { left: 40px; top: 40px; }
  .identity {
    position: absolute;
    left: 40px; top: 122px;
    padding-left: 14px;
    border-left: 6px solid var(--orange);
  }
  .person-name {
    color: var(--orange);
    font-weight: 700;
    font-size: 21px;
    letter-spacing: .02em;
    text-transform: uppercase;
  }
  .person-title {
    color: var(--muted);
    font-weight: 300;
    font-size: 15px;
    margin-top: 1px;
  }
  .contact-list {
    position: absolute;
    left: 40px; top: 208px;
    list-style: none;
    color: var(--white);
    font-weight: 400;
    font-size: 14px;
  }
  .contact-list li {
    display: flex;
    align-items: center;
    gap: 10px;
    height: 24px;
  }
  .contact-icon { width: 13px; height: 13px; flex: none; }
  .back .wordmark { right: 40px; bottom: 40px; }
  .back-pattern {
    position: absolute; inset: 0;
    background: linear-gradient(135deg, var(--pattern-dark) 0%, var(--pattern-light) 50%, var(--pattern-dark) 100%);
  }
</style>
</head>
<body>

  <section class="card front" aria-label="Card front">
    <svg class="panel-area" viewBox="0 0 630 360" role="img" aria-label="White panel where the large brand emblem sits">
      <path d="M630 150 L630 360 L300 360 C286 280 318 192 398 162 C462 138 560 138 630 150 Z" fill="var(--white)"/>
    </svg>

    <div class="wordmark">
      <span class="wordmark-dot"></span>
      <span class="wordmark-name">Sable<br>Crestway</span>
    </div>

    <div class="identity">
      <p class="person-name">Wren Tasker</p>
      <p class="person-title">Founder &amp; Principal</p>
    </div>

    <ul class="contact-list">
      <li>
        <svg class="contact-icon" viewBox="0 0 16 16" aria-hidden="true"><path d="M3.5 1.5l2.5 0 1.2 3.2-1.7 1.2c.8 1.8 2.3 3.3 4.1 4.1l1.2-1.7 3.2 1.2 0 2.5c0 .8-.7 1.5-1.5 1.5C6.9 13.5 2.5 9.1 2 3c0-.8.7-1.5 1.5-1.5z" fill="var(--orange)"/></svg>
        +1.415.836.2094
      </li>
      <li>
        <svg class="contact-icon" viewBox="0 0 16 16" aria-hidden="true"><rect x="1" y="3" width="14" height="10" rx="1.5" fill="var(--orange)"/><path d="M1.5 4l6.5 5 6.5-5" fill="none" stroke="var(--card-dark)" stroke-width="1.4"/></svg>
        wren@sablecrestway.com
      </li>
      <li>
        <svg class="contact-icon" viewBox="0 0 16 16" aria-hidden="true"><circle cx="8" cy="8" r="6.5" fill="none" stroke="var(--orange)" stroke-width="1.6"/><ellipse cx="8" cy="8" rx="2.8" ry="6.5" fill="none" stroke="var(--orange)" stroke-width="1.3"/><path d="M1.5 8h13" stroke="var(--orange)" stroke-width="1.3"/></svg>
        sablecrestway.com
      </li>
    </ul>
  </section>

  <section class="card back" aria-label="Card back">
    <div class="back-pattern" role="img" aria-label="Tone-on-tone repeating brand pattern across the whole card"></div>
    <div class="wordmark">
      <span class="wordmark-dot"></span>
      <span class="wordmark-name">Sable<br>Crestway</span>
    </div>
  </section>

</body>
</html>
```